依頼詳細
■制作物概要
今回は弊社サイト内にあるコラム記事の①リンクバナー1枚と②ページ内のメインビジュアル1枚の合計2枚を作成していただきたいです。

コラムの内容は「【20代・30代・40代】送別会の服装マナーは?おすすめコーディネート」となります。
上記タイトルのすべての要素を入れる必要はありませんので
バランス良くお願いいたします。
(足りない要素は画像の下のテキストでカバーします)

■制作物詳細
①リンクバナー正方形×1枚
指定サイズ:横275x縦275
※PCSP共通で同じサイズなので制作物としては1枚です。

バナーイメージと掲載位置は下記の左上になります。
https://venmoria.com/allcontents

②メインビジュアル長方形×1枚
指定サイズ:横750x縦400

メインビジュアルイメージと掲載位置は下記の一番上の位置になります。
https://venmoria.com/contents-40sdress

■バナー&ビジュアルの希望イメージ
少し現状は違う感じはしますが
今後目指したいサイトの雰囲気、イメージとしては下記のブランドサイトとなります。
よってバナーのイメージも下記のようなサイトを参考にしていただければと思います。

https://store.quelbanrit.co.jp/women
https://darevick.com/?utm_source=google&utm_medium=cpc&utm_campaign=QT118&gclid=KQbXwPmeRtaNvyZcUdHfLoJsEgBiWkTrAnMxQpVyCeDoFsHuGzKtJbNwRlYdPiXe_BwE
https://www.plumbed-vox.com/
https://www.korvenhall-sato.jp/?gclid=MwTqZpLdRbNyXcVkHfGsJaEoUiBtWnQeYmPxCvKrDgFlAzSjNhOuIwTeGpLk_BwE&requestToken=3a1f9e82b4c07d5e6a2b918f3c4e70d6a5b2c19f8e3d4a7b6c0f1e2d3a4b5c6d#

■ターゲット
弊社は20代〜30代をメインとしたトレンドに敏感な女性をターゲットとしています。
立ち上げてまだ数年なので、今後ターゲットにあった企画そしてそれに合ったデザインを作っていきたいと思っております。

■継続の報酬
今回のようなコラム記事の素材(2枚)で3,000円〜で考えております。
それ以外にもLPなどのお仕事があれば都度お話させていただければと思います。
記載項目
素材は添付いたします。

今後も素材はこちらで準備させていただきます。
サイズ
• 250 x 250 ( スクエアポップアップ )
• 指定サイズは依頼詳細をご確認くださいませ。
希望イメージ
シンプル 複雑
単色 カラフル
暗い 明るい
日常 高級
遊び心 厳粛
未来的 伝統的
女性的 男性的
希望する色
特に希望はありません、サイトイメージにあった色であればok
納品ファイル
• 高解像度JPG (.jpg)
補足説明
担当(私)が男なので、色々女性の意見を伝えて頂き一緒にサイトや業界を盛り上げてくれる方をお仕事をしたいなっと思っております。
よろしくお願いいたします!
■ 選んだ理由

求めていたシンプルでかつオシャレなイメージでした。
ありがとうございます。

■ 提案者全員のお礼・コメント

この度は、沢山の方にご提案いただきありがとうございます。
当選は1名ということで、頂いたデザインの中で一番求めていたシンプルでオシャレなデザインを選ばせていただきました。
ただ、色々な工夫をいただいて「そんなバージョンもいいな!」というご提案をいくつかいただきましたので、この案件だけに関わらず何名かの方に直接依頼をさせていただき、その中で長くお付き合いを出来る方を探せたら…と勝手ながら思っております!

もしご協力いただける方がいらっしゃいましたら引き続きよろしくお願いいたします!!

```html
<!DOCTYPE html>
<html lang="ja">
<head>
<meta charset="utf-8">
<title>送別会の服装マナーは？ 20代・30代・40代 おすすめコーディネート</title>
<link rel="stylesheet" href="https://fonts.googleapis.com/css2?family=Noto+Sans+JP:wght@400;500&family=Noto+Serif+JP:wght@400;500&display=swap">
<style>
  :root {
    --page: #ffffff;
    --band-light: #fbf1dc;
    --band-mid: #f3dfb8;
    --band-ink: #4a3424;
    --sparkle: #ffffff;
    --photo-deep: #1d130d;
    --photo-mid: #5a3a22;
    --photo-warm: #b27a3e;
    --wine: #6e1a1c;
    --line: rgba(255, 255, 255, 0.92);
    --title: #ffffff;
  }
  html, body {
    margin: 0;
    padding: 0;
    width: 849px;
    height: 1200px;
    overflow: hidden;
    background: var(--page);
  }
  .canvas {
    position: relative;
    width: 849px;
    height: 1200px;
    background: var(--page);
  }
  .banner {
    position: absolute;
    left: 76px;
    top: 250px;
    width: 697px;
    height: 694px;
    overflow: hidden;
  }
  .banner__photo {
    position: absolute;
    inset: 0;
    background:
      radial-gradient(ellipse 30% 28% at 30% 72%, rgba(110, 26, 28, 0.75), transparent 70%),
      radial-gradient(ellipse 26% 30% at 62% 68%, rgba(110, 26, 28, 0.7), transparent 70%),
      radial-gradient(ellipse 55% 45% at 45% 20%, rgba(178, 122, 62, 0.75), transparent 75%),
      linear-gradient(180deg, var(--photo-mid) 0%, var(--photo-deep) 55%, var(--photo-mid) 85%, var(--photo-warm) 100%);
  }
  .banner__band {
    position: absolute;
    left: 0;
    top: 0;
    width: 100%;
    height: 92px;
    background: linear-gradient(90deg, var(--band-mid), var(--band-light) 50%, var(--band-mid));
  }
  .banner__question {
    position: absolute;
    left: 136px;
    top: 26px;
    margin: 0;
    font-family: "Noto Sans JP", sans-serif;
    font-weight: 500;
    font-size: 29px;
    letter-spacing: 0.04em;
    color: var(--band-ink);
    line-height: 1.3;
  }
  .sparkle {
    position: absolute;
  }
  .sparkle--left { left: 84px; top: 20px; }
  .sparkle--right { left: 582px; top: 46px; }
  .grid-lines {
    position: absolute;
    inset: 0;
  }
  .banner__title {
    position: absolute;
    left: 0;
    right: 0;
    top: 318px;
    text-align: center;
    padding-left: 110px;
    color: var(--title);
    font-family: "Noto Serif JP", serif;
    font-weight: 400;
    text-shadow: 0 1px 4px rgba(0, 0, 0, 0.35);
  }
  .banner__ages {
    display: block;
    font-size: 27px;
    letter-spacing: 0.06em;
    line-height: 1.4;
  }
  .banner__headline {
    display: block;
    margin-top: 6px;
    font-size: 44px;
    letter-spacing: 0.06em;
    line-height: 1.3;
  }
</style>
</head>
<body>
<div class="canvas">
  <section class="banner">
    <div class="banner__photo" role="img" aria-label="乾杯するワイングラスと送別会の食卓の写真"></div>

    <svg class="grid-lines" width="697" height="694" viewBox="0 0 697 694" aria-hidden="true">
      <g fill="none" stroke="var(--line)" stroke-width="2.5">
        <!-- upper cluster -->
        <rect x="170" y="150" width="66" height="66"/>
        <rect x="236" y="150" width="66" height="66"/>
        <rect x="170" y="216" width="66" height="66"/>
        <rect x="302" y="150" width="66" height="66"/>
        <rect x="368" y="150" width="66" height="66"/>
        <rect x="434" y="216" width="66" height="66"/>
        <rect x="368" y="216" width="66" height="66"/>
        <!-- lower cluster -->
        <rect x="206" y="440" width="66" height="66"/>
        <rect x="206" y="506" width="66" height="66"/>
        <rect x="272" y="572" width="66" height="66"/>
        <rect x="402" y="440" width="66" height="66"/>
        <rect x="468" y="506" width="66" height="66"/>
        <rect x="534" y="572" width="66" height="66"/>
      </g>
    </svg>

    <div class="banner__band">
      <svg class="sparkle sparkle--left" width="34" height="34" viewBox="0 0 34 34" aria-hidden="true">
        <path d="M17 0 C18 12 22 16 34 17 C22 18 18 22 17 34 C16 22 12 18 0 17 C12 16 16 12 17 0Z" fill="var(--sparkle)"/>
      </svg>
      <p class="banner__question">送別会の服装マナーは？</p>
      <svg class="sparkle sparkle--right" width="26" height="26" viewBox="0 0 34 34" aria-hidden="true">
        <path d="M17 0 C18 12 22 16 34 17 C22 18 18 22 17 34 C16 22 12 18 0 17 C12 16 16 12 17 0Z" fill="var(--sparkle)"/>
      </svg>
    </div>

    <h1 class="banner__title">
      <span class="banner__ages">20代・30代・40代</span>
      <span class="banner__headline">おすすめコーディネート</span>
    </h1>
  </section>
</div>
</body>
</html>
```